design a beautiful, neat and professional looking 10 page templete for an online course

I designed an online course. It about the newborn adoption process. I need you to design the template for it. Just the first 10 pages is enough. I'm thinking a neutral palette with a pop of a minor color to keep it from being boring. The pop of color should not distract the reader. You can design how you want. If you want to add small details or hearts or a shape in background you can. Just dont overdo it. Sparingly is the key. You can make pages a different color. It just needs to look like a neutral color palette with a small pop of color.
Updates

Low design quality

Target Market(s)

people who are adopting a newborn in the USA

Industry/Entity Type

newborn adoption

Font styles to use
Sans Serif

Colors

Designer to choose colors to be used in the design.

Requirements
Should not have
• bold or distracting colors or patterns

```html
<!DOCTYPE html>
<html lang="en">
<head>
<meta charset="utf-8">
<title>Newborn Adoption Process – Course Template</title>
<link rel="stylesheet" href="https://fonts.googleapis.com/css2?family=Montserrat:wght@400;500;600;700&family=Roboto:wght@400;500;700&display=swap">
<style>
:root{
  --page:#e8e9eb;
  --paper:#ffffff;
  --mint:#98ded1;
  --mint-soft:#cdeee8;
  --blue:#a8c4f4;
  --blue-deep:#8fb2ef;
  --ink:#3a3f47;
  --gray:#8b9097;
  --line:#e3e5e8;
  --photo-warm:#e9dccf;
  --photo-cool:#d9dde3;
}
*{box-sizing:border-box;margin:0;padding:0}
html,body{width:1200px;height:1176px;overflow:hidden;background:var(--page)}
body{position:relative;font-family:"Montserrat",Arial,sans-serif;color:var(--ink)}
.slide{position:absolute;width:365px;height:204px;background:var(--paper);box-shadow:0 2px 5px rgba(0,0,0,.18);overflow:hidden}
.slide>*{position:absolute}
.slide::after{content:"";position:absolute;left:0;right:0;bottom:0;height:1.5px;background:var(--mint)}
.no-rule::after{display:none}
.foot-band{left:0;bottom:0;height:9px;width:108px;background:var(--blue);clip-path:polygon(0 0,91% 0,100% 100%,0 100%);font-size:3.2px;letter-spacing:1.3px;color:#fff;line-height:9px;padding-left:12px;z-index:2}
.page-no{right:8px;bottom:6px;font-size:3.6px;color:var(--ink)}
.corner{width:8px;height:8px;background:var(--blue)}
.corner.mint{background:var(--mint)}
.title{font-weight:600;font-size:11px;color:var(--ink);white-space:nowrap}
.title-lg{font-weight:600;font-size:13px;line-height:1.3;color:var(--ink)}
.bar{height:2px;width:25px;background:var(--blue)}
.p{font-size:3.4px;line-height:1.4;color:var(--gray)}
.p-md{font-size:5.4px;line-height:1.3;color:var(--gray)}
.h{font-size:6.6px;font-weight:600;color:var(--ink);white-space:nowrap}
.photo{border-radius:0}
.photo-warm{background:linear-gradient(135deg,#f1e6da,#d8c2ae)}
.photo-soft{background:linear-gradient(135deg,#f3ece6,#dccbbd)}
.photo-gray{background:linear-gradient(135deg,#ece6e0,#c9bfb6)}
.photo-blue{background:linear-gradient(135deg,#bcd0f6,#9ab8ee)}
.full{left:0;top:0;width:365px;height:204px}
.num{color:var(--mint);font-weight:600}
.mint-t{color:var(--mint)}
.blue-t{color:var(--blue-deep)}
.roboto{font-family:"Roboto",Arial,sans-serif}
svg text{font-family:"Montserrat",Arial,sans-serif}
</style>
</head>
<body>

<!-- 1 Cover -->
<section class="slide no-rule" style="left:43px;top:49px">
  <div class="corner" style="left:8px;top:8px"></div>
  <div class="photo photo-soft" role="img" aria-label="Newborn baby in a knitted hat lying on a soft blanket" style="left:152px;top:0;width:213px;height:178px"></div>
  <div style="left:152px;top:178px;width:213px;height:26px;background:var(--mint-soft);font-size:5px;letter-spacing:2.4px;color:#fff;text-align:center;line-height:26px">www.nestcourse.com</div>
  <svg style="left:140px;top:50px" width="24" height="6"><g fill="var(--ink)"><circle cx="2" cy="1.5" r=".9"/><circle cx="6" cy="1.5" r=".9"/><circle cx="10" cy="1.5" r=".9"/><circle cx="14" cy="1.5" r=".9"/><circle cx="18" cy="1.5" r=".9"/><circle cx="2" cy="4.5" r=".9"/><circle cx="6" cy="4.5" r=".9"/><circle cx="10" cy="4.5" r=".9"/><circle cx="14" cy="4.5" r=".9"/><circle cx="18" cy="4.5" r=".9"/></g></svg>
  <div class="roboto" style="left:20px;top:57px;font-size:14px;color:var(--ink)">Newborn</div>
  <div class="roboto" style="left:19px;top:70px;font-size:27px;font-weight:700;color:var(--blue-deep)">Adoption</div>
  <div class="roboto" style="left:20px;top:99px;font-size:21px;color:var(--mint)">Process</div>
  <p class="p" style="left:20px;top:135px;width:112px">Lorem ipsum dolor sit amet, consectetuer adipiscing elit, sed diam nonummy nibh euismod tincidunt ut laoreet dolore magna aliquam erat volutpat. Ut wisi enim ad minim veniam, quis nostrud exerci tation ullamcorper suscipit lobortis nisl ut aliquip ex ea commodo. Duis autem vel eum iriure</p>
</section>

<!-- 2 List with photo -->
<section class="slide" style="left:419px;top:49px">
  <div class="title" style="left:11px;top:14px">Text Added Here</div>
  <div class="bar" style="left:11px;top:32px"></div>
  <div style="left:30px;top:90px;width:142px;height:82px;border:5px solid var(--line);border-top:none"></div>
  <div class="photo photo-warm" role="img" aria-label="Mother lying in bed holding her newborn" style="left:45px;top:49px;width:105px;height:115px"></div>
  <div style="left:184px;top:49px">
    <div class="h" style="font-size:7px"><span class="num">1.</span> Lorem ipsum</div>
    <p class="p" style="width:145px;margin:2px 0 0 10px">Lorem ipsum dolor sit amet, consectetuer adipiscing elit, sed diam nonummy nibh euismod tincid</p>
  </div>
  <div style="left:184px;top:85px">
    <div class="h" style="font-size:7px"><span class="num">2.</span> Lorem ipsum</div>
    <p class="p" style="width:145px;margin:2px 0 0 10px">Lorem ipsum dolor sit amet, consectetuer adipiscing elit, sed diam nonummy nibh euismod tincid</p>
  </div>
  <div style="left:184px;top:121px">
    <div class="h" style="font-size:7px"><span class="num">3.</span> Lorem ipsum</div>
    <p class="p" style="width:145px;margin:2px 0 0 10px">Lorem ipsum dolor sit amet, consectetuer adipiscing elit, sed diam nonummy nibh euismod tincid</p>
  </div>
  <div style="left:184px;top:155px">
    <div class="h" style="font-size:7px"><span class="num">4.</span> Lorem ipsum</div>
    <p class="p" style="width:145px;margin:2px 0 0 10px">Lorem ipsum dolor sit amet, consectetuer adipiscing elit, sed diam nonummy nibh euismod tincid</p>
  </div>
  <div class="foot-band">www.nestcourse.com</div><div class="page-no">2</div>
</section>

<!-- 3 Intro -->
<section class="slide" style="left:793px;top:49px">
  <div class="title-lg" style="left:22px;top:26px">Lorem Ipsum<br>Dolor Sit<br>Ametkeeper.</div>
  <div class="bar" style="left:22px;top:82px"></div>
  <p class="p" style="left:22px;top:94px;width:106px">Lorem ipsum dolor sit amet, consectetuer adipiscing elit, sed diam nonummy nibh euismod tincidunt ut laoreet dolore magna aliquam erat volutpat.</p>
  <p class="p" style="left:22px;top:122px;width:106px">Ut wisi enim ad minim veniam, quis nostrud exerci tation ullamcorper suscipit lobortis nisl ut aliquip ex ea commodo consequat. Duis autem vel eum iriure dolor in hendrerit in vulputate velit esse molestie consequat.</p>
  <p class="p" style="left:22px;top:162px;width:106px">vel illum dolore eu feugiat nulla facilisis at vero eros et accumsan et iusto odio</p>
  <div style="left:175px;top:29px;width:168px;height:3px;background:var(--mint-soft)"></div>
  <div class="photo photo-warm" role="img" aria-label="Close-up of a sleeping newborn on a white sheet" style="left:144px;top:32px;width:221px;height:91px"></div>
  <div style="left:175px;top:122px;width:168px;height:3px;background:var(--mint-soft)"></div>
  <p class="p" style="left:143px;top:133px;width:195px">Lorem ipsum dolor sit amet, consectetuer adipiscing elit, sed diam nonummy nibh euismod tincidunt erat volutpat.</p>
  <p class="p" style="left:143px;top:149px;width:195px">Ut wisi enim ad minim veniam, quis nostrud exerci tation ullamcorper suscipit lobortis nisl ut aliquip ex ea commodo consequat. Ut wisi enim ad minim veniam, quis nostrud exerci tation ullamcorper suscipit lobortis nisl ut aliquip ex ea commodo consequat.</p>
  <div class="foot-band">www.nestcourse.com</div><div class="page-no">3</div>
</section>

<!-- 4 Values -->
<section class="slide" style="left:43px;top:264px">
  <div class="corner" style="left:8px;top:8px"></div>
  <div class="title-lg" style="left:24px;top:32px;font-size:15px;line-height:1.45">Lorem Ipsum<br>Dolor Sit<br>Ametkeeper.</div>
  <p class="p" style="left:24px;top:111px;width:105px">Lorem ipsum dolor sit amet, consectetuer adipiscing elit, sed diam nonummy nibh euismod tincidunt erat volutpat.</p>
  <p class="p" style="left:24px;top:141px;width:105px">Ut wisi enim ad minim veniam, quis nostrud exerci tation ullamcorper suscipit lobortis nisl ut aliquip ex ea commodo consequat.</p>

  <div style="left:159px;top:39px;width:29px;height:29px;background:var(--mint)"></div>
  <svg style="left:159px;top:39px" width="29" height="29"><g fill="#fff"><circle cx="14.5" cy="11" r="3"/><circle cx="9" cy="12.5" r="2.2"/><circle cx="20" cy="12.5" r="2.2"/><path d="M9.5 21c0-4 2.3-6 5-6s5 2 5 6z"/><path d="M5 20c0-3 1.6-4.5 4-4.5 1 0 1.6.3 2 .7-1 1-1.6 2.3-1.7 3.8z"/><path d="M24 20c0-3-1.6-4.5-4-4.5-1 0-1.6.3-2 .7 1 1 1.6 2.3 1.7 3.8z"/></g></svg>
  <div class="h" style="left:200px;top:42px;font-size:8px">We Before Me</div>
  <p class="p" style="left:200px;top:53px;width:135px">ipsum dolor sit amet, cons ectetuer adipiscing elit, sed diam nonummy nibh euismod tincidunt ut laoreet</p>

  <div style="left:159px;top:88px;width:29px;height:29px;background:var(--mint)"></div>
  <svg style="left:159px;top:88px" width="29" height="29"><g fill="#fff"><circle cx="11" cy="7" r="2.3"/><circle cx="18" cy="7" r="2.3"/><rect x="8.5" y="10" width="5" height="9" rx="1.5"/><rect x="15.5" y="10" width="5" height="9" rx="1.5"/><rect x="9.3" y="18" width="1.6" height="6"/><rect x="11.2" y="18" width="1.6" height="6"/><rect x="16.3" y="18" width="1.6" height="6"/><rect x="18.2" y="18" width="1.6" height="6"/></g></svg>
  <div class="h" style="left:199px;top:91px;font-size:8px">We Are Good People</div>
  <p class="p" style="left:199px;top:102px;width:145px">ipsum dolor sit amet, cons ectetuer adipiscing elit, sed diam nonummy nibh euismod tincidunt ut laoreet dolore magna aliquam erat volutpat.</p>

  <div style="left:159px;top:142px;width:29px;height:29px;background:var(--mint)"></div>
  <svg style="left:159px;top:142px" width="29" height="29"><g fill="#fff"><path d="M14.5 16 10 11.6a2.6 2.6 0 0 1 4.5-2.5 2.6 2.6 0 0 1 4.5 2.5z"/><path d="M5 19h4l3 1.5h5l2-1.5 4-2 1 1-5 4.5h-7l-3-1H5z"/></g></svg>
  <div class="h" style="left:199px;top:145px;font-size:8px">We Work with Heart</div>
  <p class="p" style="left:199px;top:156px;width:135px">ipsum dolor sit amet, cons ectetuer adipiscing elit, sed diam nonummy nibh euismod tincidunt</p>
  <div class="foot-band">www.nestcourse.com</div><div class="page-no">4</div>
</section>

<!-- 5 Education -->
<section class="slide" style="left:419px;top:264px">
  <div class="title" style="left:11px;top:12px">Our Education</div>
  <div class="bar" style="left:11px;top:30px"></div>
  <div role="img" aria-label="Faint world map in the background" style="left:55px;top:34px;width:260px;height:128px;background:radial-gradient(ellipse at center,#f1f2f4 0%,#f6f7f8 60%,#fff 100%)"></div>
  <svg class="full" viewBox="0 0 365 204">
    <g fill="none" stroke="#45494f" stroke-width="2.4" stroke-linejoin="round">
      <path d="M120 54H70a4 4 0 0 0-4 4v87a4 4 0 0 0 4 4h54a4 4 0 0 0 4-4V130"/>
      <path d="M124 54a4 4 0 0 1 4 4v20"/>
      <path d="M127 79 151 124"/>
      <path d="M151 124v21a4 4 0 0 0 4 4h53a4 4 0 0 0 4-4V58a4 4 0 0 0-4-4H155a4 4 0 0 0-4 4v40"/>
      <path d="M208 54a4 4 0 0 1 4 4v20"/>
      <path d="M212 79 235 124"/>
      <path d="M235 124v21a4 4 0 0 0 4 4h54a4 4 0 0 0 4-4V58a4 4 0 0 0-4-4H239a4 4 0 0 0-4 4v40"/>
    </g>
    <g fill="#45494f"><circle cx="127" cy="79" r="3"/><circle cx="151" cy="124" r="3"/><circle cx="212" cy="79" r="3"/><circle cx="235" cy="124" r="3"/></g>
    <g fill="none" stroke="var(--mint)" stroke-width="1">
      <path d="M95 66a4 4 0 1 1 3 0v3h-3z"/><path d="M95.5 71h2"/>
      <rect x="176" y="69" width="10" height="7"/><path d="M176 69l5 4 5-4"/>
      <path d="M261 75l4-4 3 3 4-5M259 67v9h13"/>
    </g>
    <g font-size="5.6" font-weight="600" fill="var(--gray)" text-anchor="middle">
      <text x="97" y="88">IDEA</text><text x="181" y="89">PROMOTION</text><text x="266" y="88">GROWTH</text>
    </g>
    <g font-size="3" fill="var(--gray)" text-anchor="middle">
      <text x="97" y="95">Lorem ipsum dolor sit amet,</text><text x="97" y="99">consectetuer adipiscing elit,</text><text x="97" y="103">sed diam nonummy nibh</text><text x="97" y="107">euismod tincidunt ut</text><text x="97" y="111">laoreet dolore magna</text><text x="97" y="115">aliquam erat volutpat. Ut</text><text x="97" y="119">wisi enim ad minim veniam,</text><text x="97" y="123">quis nostrud exerci tation</text><text x="97" y="127">ullamcorper suscipit lobortis</text><text x="97" y="131">nisl ut aliquip ex ea</text>
      <text x="181" y="95">Lorem ipsum dolor sit amet,</text><text x="181" y="99">consectetuer adipiscing elit,</text><text x="181" y="103">sed diam nonummy nibh</text><text x="181" y="107">euismod tincidunt ut</text><text x="181" y="111">laoreet dolore magna</text><text x="181" y="115">aliquam erat volutpat. Ut</text><text x="181" y="119">wisi enim ad minim veniam,</text><text x="181" y="123">quis nostrud exerci tation</text><text x="181" y="127">ullamcorper suscipit lobortis</text><text x="181" y="131">nisl ut aliquip ex ea</text>
      <text x="266" y="95">Lorem ipsum dolor sit amet,</text><text x="266" y="99">consectetuer adipiscing elit,</text><text x="266" y="103">sed diam nonummy nibh</text><text x="266" y="107">euismod tincidunt ut</text><text x="266" y="111">laoreet dolore magna</text><text x="266" y="115">aliquam erat volutpat. Ut</text><text x="266" y="119">wisi enim ad minim veniam,</text><text x="266" y="123">quis nostrud exerci tation</text><text x="266" y="127">ullamcorper suscipit lobortis</text><text x="266" y="131">nisl ut aliquip ex ea</text>
    </g>
  </svg>
  <p class="p" style="left:42px;top:160px;width:282px;text-align:center;font-size:3.7px">Lorem ipsum dolor sit amet, consectetuer adipiscing elit, sed diam nonummy nibh euismod tincidunt ut laoreet dolore magna aliquam erat volutpat. Ut wisi enim ad minim veniam, quis nostrud exerci tation ullamcorper suscipit lobortis nisl ut aliquip ex ea commodo consequat. Duis autem vel eum iriure dolor in hendrerit i</p>
  <div class="foot-band">www.nestcourse.com</div><div class="page-no">5</div>
</section>

<!-- 6 Subject -->
<section class="slide" style="left:793px;top:264px">
  <div style="left:0;top:0;width:103px;height:13px;background:var(--mint-soft)"></div>
  <div class="title-lg" style="left:20px;top:31px">Subject<br>Title Added</div>
  <div class="bar" style="left:20px;top:74px"></div>
  <p class="p" style="left:20px;top:85px;width:80px;font-size:4.4px;line-height:1.65">Lorem ipsum dolor sit amet, consectetuer adipiscing elit, sed diam nonummy nibh euismod tincidunt ut laoreet dolore magna aliquam erat volutpat. Ut wisi enim ad minim veniam, quis nostrud exerci tation ullamcorper suscipit lobortis nisl ut aliquip ex ea commodo consequat. Duis autem vel eum iriure.</p>
  <div class="photo photo-gray" role="img" aria-label="Mother holding her baby by a window" style="left:103px;top:0;width:74px;height:127px"></div>
  <div style="left:153px;top:44px;width:212px;height:124px;background:var(--blue)"></div>
  <div class="photo photo-gray" role="img" aria-label="Baby sleeping under a knitted blanket" style="left:188px;top:64px;width:75px;height:122px"></div>
  <div style="left:270px;top:72px;font-size:9.5px;font-weight:500;color:#fff;line-height:1.3">Lorem Ipsum<br>Dolor Sit<br>Ametkeeper.</div>
  <p class="p" style="left:270px;top:114px;width:80px;color:#fff">Lorem ipsum dolor sit amet, consectetuer adipiscing</p>
  <p class="p" style="left:270px;top:128px;width:80px;color:#fff">elit, sed diam nonummy nibh euismod tincidunt ut laoreet dolore magna aliquam erat volutpat. Ut wisi enim ad minim veniam, quis nostrud exerci tation ut aliquip</p>
  <div class="foot-band">www.nestcourse.com</div><div class="page-no">6</div>
</section>

<!-- 7 Steps with photo -->
<section class="slide" style="left:43px;top:479px">
  <div class="corner" style="left:8px;top:8px"></div>
  <div class="title" style="left:30px;top:24px">Text Added Here</div>
  <div style="left:47px;top:42px;width:46px;height:4px;background:var(--blue)"></div>
  <div class="photo photo-warm" role="img" aria-label="Smiling parents cuddling their newborn" style="left:23px;top:45px;width:110px;height:128px"></div>
  <svg class="full" viewBox="0 0 365 204">
    <g fill="var(--mint)"><circle cx="164" cy="63" r="11"/><circle cx="164" cy="106" r="11"/><circle cx="164" cy="150" r="11"/></g>
    <g fill="#fff" font-size="9" font-weight="600" text-anchor="middle"><text x="164" y="66.5">1</text><text x="164" y="109.5">2</text><text x="164" y="153.5">3</text></g>
  </svg>
  <p class="p-md" style="left:193px;top:52px;width:158px;font-size:4.4px;text-align:justify">Lorem ipsum dolor sit amet, consectetuer adipiscing elit, sed diam nonummy nibh euismod tincidunt ut laoreet dolore magna aliquam erat volutpat. Ut wisi enim ad minim veniam, quis nostrud</p>
  <p class="p-md" style="left:193px;top:94px;width:158px;font-size:4.4px">ullamcorper suscipit lobortis nisl ut aliquip ex ea commodo consequat. Duis autem vel eum iriure dolor in hendrerit in vulputate velit esse molestie consequat, vel illum dolore eu feugiat nulla facilisis at vero eros et accumsan et iusto odio dignissim qui</p>
  <p class="p-md" style="left:193px;top:142px;width:158px;font-size:4.4px;text-align:justify">Lorem ipsum dolor sit amet, consectetuer adipiscing elit, sed diam nonummy nibh euismod tincidunt ut laoreet dolore magna aliquam erat volutpat. Ut wisi enim ad minim veniam, quis nostrud</p>
  <div class="foot-band">www.nestcourse.com</div><div class="page-no">7</div>
</section>

<!-- 8 Market chart -->
<section class="slide" style="left:419px;top:479px">
  <div class="corner" style="left:8px;top:8px"></div>
  <div class="title-lg" style="left:19px;top:24px">Market<br>Opportunities.</div>
  <p class="p-md" style="left:19px;top:62px;width:92px;font-size:5.5px;line-height:1.28">Lorem ipsum dolor sit amet, consectetuer adipiscing elit, sed diam nonummy nibh euismod tincidunt ut laoreet dolore magna aliquam erat volutpat. Ut wisi enim ad minim veniam, quis nostrud exerci tation ullamcorper suscipit lobortis nisl ut aliquip ex ea commodo consequat. Duis autem vel eum iriure dolor in hendrerit i</p>
  <p class="p-md" style="left:19px;top:156px;width:92px;font-size:5.5px;line-height:1.28">Lorem ipsum dolor sit amet, consectetuer adipiscing elit, sed diam nonummy nibh .</p>
  <div style="left:146px;top:30px;font-size:5.6px;font-weight:500;color:var(--ink)">CONSECTETUER ADIPISCING</div>
  <svg class="full" viewBox="0 0 365 204">
    <g stroke="#cfd2d6" stroke-width=".5">
      <line x1="153" y1="48" x2="332" y2="48"/><line x1="153" y1="62.2" x2="332" y2="62.2"/><line x1="153" y1="76.3" x2="332" y2="76.3"/><line x1="153" y1="90.5" x2="332" y2="90.5"/><line x1="153" y1="104.7" x2="332" y2="104.7"/><line x1="153" y1="118.8" x2="332" y2="118.8"/><line x1="153" y1="133" x2="332" y2="133"/>
      <line x1="153" y1="48" x2="153" y2="133"/><line x1="332" y1="48" x2="332" y2="133"/>
    </g>
    <g font-size="5.4" fill="var(--ink)" text-anchor="end">
      <text x="150" y="50">60</text><text x="150" y="64">50</text><text x="150" y="78">40</text><text x="150" y="92">30</text><text x="150" y="106.5">20</text><text x="150" y="120.5">10</text><text x="150" y="135">0</text>
    </g>
    <rect x="171" y="56.5" width="20" height="76.5" fill="var(--blue)"/>
    <rect x="210" y="88" width="20" height="45" fill="var(--mint)"/>
    <rect x="248" y="66.4" width="20" height="66.6" fill="var(--blue)"/>
    <rect x="287" y="95" width="20" height="38" fill="var(--mint)"/>
    <g font-size="5.6" fill="var(--ink)" text-anchor="middle"><text x="181" y="145">JAN</text><text x="220" y="145">FEB</text><text x="258" y="145">MAR</text><text x="297" y="145">APR</text></g>
    <circle cx="141" cy="164" r="3" fill="var(--mint)"/><circle cx="247" cy="164" r="3" fill="var(--blue)"/>
    <g font-size="6.4" font-weight="500" fill="var(--ink)"><text x="152" y="166">Lorem ipsum</text><text x="257" y="166">Lorem ipsum</text></g>
    <g font-size="3.4" fill="var(--gray)">
      <text x="152" y="172">Lorem ipsum dolor sit amet, consectetuer</text><text x="152" y="176.5">adipiscing elit, sed diam nonummy nibh</text><text x="152" y="181">euismod tincidunt ut laoreet</text>
      <text x="257" y="172">Lorem ipsum dolor sit amet, consectetuer</text><text x="257" y="176.5">adipiscing elit, sed diam nonummy nibh</text><text x="257" y="181">euismod tincidunt ut laoreet</text>
    </g>
  </svg>
  <div class="foot-band">www.nestcourse.com</div><div class="page-no">8</div>
</section>

<!-- 9 Cycle -->
<section class="slide" style="left:793px;top:479px">
  <div class="title-lg" style="left:19px;top:16px;font-size:13px">Subtitle Text</div>
  <p class="p" style="left:19px;top:46px;width:100px;font-size:3.8px">Lorem ipsum dolor sit amet, consectetuer adipiscing elit, sed diam nonummy nibh .</p>
  <p class="p" style="left:19px;top:73px;width:100px;font-size:3.8px">Ut wisi enim ad minim veniam, quis nostrud exerci tation ullamcorper suscipit lobortis.</p>
  <svg class="full" viewBox="0 0 365 204">
    <g fill="var(--mint)"><circle cx="22" cy="109" r="2.3"/><circle cx="22" cy="135" r="2.3"/><circle cx="22" cy="162" r="2.3"/></g>
    <g font-size="5" fill="var(--ink)"><text x="30" y="111">Lorem ipsum</text><text x="30" y="137">Lorem ipsum</text><text x="30" y="164">Lorem ipsum</text></g>
    <g font-size="2.8" fill="var(--gray)">
      <text x="30" y="116">Lorem ipsum dolor sit amet,</text><text x="30" y="119.5">consectetuer adipiscing elit, sed diam</text><text x="30" y="123">nonummy nibh euismod tincidunt ut</text>
      <text x="30" y="142">Lorem ipsum dolor sit amet,</text><text x="30" y="145.5">consectetuer adipiscing elit, sed diam</text><text x="30" y="149">nonummy nibh euismod tincidunt ut</text>
      <text x="30" y="169">Lorem ipsum dolor sit amet,</text><text x="30" y="172.5">consectetuer adipiscing elit, sed diam</text><text x="30" y="176">nonummy nibh euismod tincidunt ut</text>
    </g>
    <path d="M176 93A57 57 0 1 1 180 127" fill="none" stroke="#3d4148" stroke-width="3"/>
    <path d="M169 85l7 10 6-10" fill="none" stroke="#3d4148" stroke-width="2.4"/>
    <circle cx="180" cy="127" r="3.4" fill="#3d4148"/>
    <g>
      <circle cx="270" cy="62" r="16" fill="#fff" stroke="var(--line)" stroke-width="1"/>
      <circle cx="270" cy="62" r="12" fill="none" stroke="var(--mint)" stroke-width="4"/>
      <circle cx="269" cy="61" r="3" fill="none" stroke="#3d4148" stroke-width="1.2"/><path d="M266.8 63.2l-2.5 2.5" stroke="#3d4148" stroke-width="1.4"/>
      <circle cx="285" cy="117" r="15" fill="#fff" stroke="var(--line)" stroke-width="1"/>
      <circle cx="285" cy="117" r="11" fill="none" stroke="var(--blue)" stroke-width="4"/>
      <circle cx="285" cy="115.5" r="3" fill="#3d4148"/><rect x="283.8" y="118" width="2.4" height="2" fill="#3d4148"/>
      <circle cx="254" cy="156" r="12" fill="#fff" stroke="var(--line)" stroke-width="1"/>
      <circle cx="254" cy="156" r="8.5" fill="none" stroke="var(--mint)" stroke-width="3"/>
      <path d="M254 151.5v8M251 154h6M250.5 157.5c1 2.5 6 2.5 7 0" fill="none" stroke="#3d4148" stroke-width="1"/>
      <circle cx="180" cy="143" r="9" fill="#fff" stroke="var(--line)" stroke-width="1"/>
      <circle cx="180" cy="143" r="6.5" fill="none" stroke="var(--blue)" stroke-width="2.4"/>
      <circle cx="180" cy="144" r="2.3" fill="#3d4148"/>
    </g>
    <g stroke="var(--blue)" stroke-width=".5" fill="none"><path d="M284 50l12-5"/><path d="M270 101l-10-3"/><path d="M190 140l10-3"/><path d="M264 166l9 4"/></g>
    <g font-size="3.2" fill="var(--blue-deep)"><text x="297" y="45">85%</text><text x="248" y="98">80%</text><text x="201" y="138">50%</text><text x="274" y="172">75%</text></g>
    <rect x="226" y="87" width="2" height="7" fill="var(--blue)"/><rect x="229" y="84" width="2" height="10" fill="var(--blue)"/><rect x="232" y="89" width="2" height="5" fill="var(--blue)"/><rect x="235" y="86" width="2" height="8" fill="var(--blue)"/>
    <text x="228" y="100" font-size="5.2" font-weight="600" fill="var(--ink)" text-anchor="middle">MAIN TITLE</text>
    <g font-size="2.6" fill="var(--gray)" text-anchor="middle"><text x="228" y="104">Lorem ipsum dolor sit amet,</text><text x="228" y="107">consectetuer adipiscing elit,</text><text x="228" y="110">sed diam nonummy nibh</text></g>
    <g font-size="4.8" font-weight="500" fill="var(--ink)" text-anchor="end"><text x="343" y="56">Your Title</text><text x="350" y="108">Your Title</text><text x="161" y="141">Your Title</text><text x="341" y="154">Your Title</text></g>
    <g font-size="2.4" fill="var(--gray)" text-anchor="end">
      <text x="343" y="60">Lorem ipsum dolor sit amet,</text><text x="343" y="63">consectetuer adipiscing elit,</text><text x="343" y="66">sed diam nonummy nibh</text>
      <text x="350" y="112">Lorem ipsum dolor sit amet,</text><text x="350" y="115">consectetuer adipiscing elit,</text><text x="350" y="118">sed diam nonummy nibh</text>
      <text x="161" y="145">Lorem ipsum dolor sit amet,</text><text x="161" y="148">consectetuer adipiscing elit,</text><text x="161" y="151">sed diam nonummy nibh</text>
      <text x="341" y="158">Lorem ipsum dolor sit amet,</text><text x="341" y="161">consectetuer adipiscing elit,</text><text x="341" y="164">sed diam nonummy nibh</text>
    </g>
  </svg>
  <div class="foot-band">www.nestcourse.com</div><div class="page-no">9</div>
</section>

<!-- 10 Timeline -->
<section class="slide" style="left:43px;top:693px">
  <div class="title" style="left:11px;top:12px">Company Timeline</div>
  <div class="bar" style="left:11px;top:30px"></div>
  <svg class="full" viewBox="0 0 365 204">
    <g font-size="7.2" fill="var(--ink)">
      <text x="57" y="46">01</text><text x="98" y="46">02</text><text x="139" y="46">03</text><text x="179" y="46">04</text><text x="220" y="46">05</text><text x="262" y="46">06</text>
      <text x="57" y="155">12</text><text x="98" y="155">11</text><text x="139" y="155">10</text><text x="179" y="155">09</text><text x="220" y="155">08</text><text x="262" y="155">07</text>
    </g>
    <g font-size="2.5" fill="var(--gray)">
      <text x="57" y="52">Lorem ipsum dolor sit</text><text x="57" y="55">amet, consectetuer</text><text x="57" y="58">adipiscing elit, sed</text><text x="57" y="61">diam nonummy nibh</text>
      <text x="98" y="52">Lorem ipsum dolor sit</text><text x="98" y="55">amet, consectetuer</text><text x="98" y="58">adipiscing elit, sed</text>
      <text x="139" y="52">Lorem ipsum dolor sit</text><text x="139" y="55">amet, consectetuer</text><text x="139" y="58">adipiscing elit, sed</text><text x="139" y="61">diam nonummy nibh</text>
      <text x="179" y="52">Lorem ipsum dolor sit</text><text x="179" y="55">amet, consectetuer</text><text x="179" y="58">adipiscing elit, sed</text><text x="179" y="61">diam nonummy nibh</text>
      <text x="220" y="52">Lorem ipsum dolor sit</text><text x="220" y="55">amet, consectetuer</text><text x="220" y="58">adipiscing elit, sed</text>
      <text x="262" y="52">Lorem ipsum dolor</text><text x="262" y="55">sit amet,</text><text x="262" y="58">consectetuer</text><text x="262" y="61">adipiscing elit, sed</text>
      <text x="57" y="161">Lorem ipsum dolor sit</text><text x="57" y="164">amet, consectetuer</text><text x="57" y="167">adipiscing elit, sed</text><text x="57" y="170">diam nonummy nibh</text>
      <text x="98" y="161">Lorem ipsum dolor sit</text><text x="98" y="164">amet, consectetuer</text><text x="98" y="167">adipiscing elit, sed</text><text x="98" y="170">diam nonummy nibh</text>
      <text x="139" y="161">Lorem ipsum dolor sit</text><text x="139" y="164">amet, consectetuer</text><text x="139" y="167">adipiscing elit, sed</text><text x="139" y="170">diam nonummy nibh</text>
      <text x="179" y="161">Lorem ipsum dolor sit</text><text x="179" y="164">amet, consectetuer</text><text x="179" y="167">adipiscing elit, sed</text><text x="179" y="170">diam nonummy nibh</text>
      <text x="220" y="161">Lorem ipsum dolor sit</text><text x="220" y="164">amet, consectetuer</text><text x="220" y="167">adipiscing elit, sed</text><text x="220" y="170">diam nonummy nibh</text>
      <text x="262" y="161">Lorem ipsum dolor</text><text x="262" y="164">sit amet,</text><text x="262" y="167">consectetuer</text><text x="262" y="170">adipiscing elit, sed</text><text x="262" y="173">diam nonummy nibh</text>
    </g>
    <g fill="#eceef0">
      <path d="M57 86h28l4 7-4 7H57l4-7z"/><path d="M98 86h28l4 7-4 7H98l4-7z"/><path d="M139 86h28l4 7-4 7h-28l4-7z"/><path d="M179 86h28l4 7-4 7h-28l4-7z"/><path d="M220 86h28l4 7-4 7h-28l4-7z"/><path d="M261 86h28l4 7-4 7h-28l4-7z"/>
      <path d="M57 116h28l4 7-4 7H57l4-7z"/><path d="M98 116h28l4 7-4 7H98l4-7z"/><path d="M139 116h28l4 7-4 7h-28l4-7z"/><path d="M179 116h28l4 7-4 7h-28l4-7z"/><path d="M220 116h28l4 7-4 7h-28l4-7z"/><path d="M261 116h28l4 7-4 7h-28l4-7z"/>
    </g>
    <path d="M34 82h16" stroke="#4a4e55" stroke-width="1" stroke-dasharray="5 3"/>
    <path d="M50 82h238a28 28 0 0 1 0 52H52" fill="none" stroke="#4a4e55" stroke-width="1.2"/>
    <path d="M46 134h6" stroke="#4a4e55" stroke-width="1" stroke-dasharray="2 2"/>
    <g fill="#4a6a80">
      <circle cx="72" cy="82" r="2.2"/><circle cx="113" cy="82" r="2.2"/><circle cx="154" cy="82" r="2.2"/><circle cx="195" cy="82" r="2.2"/><circle cx="236" cy="82" r="2.2"/><circle cx="277" cy="82" r="2.2"/>
      <circle cx="72" cy="134" r="2.2"/><circle cx="113" cy="134" r="2.2"/><circle cx="154" cy="134" r="2.2"/><circle cx="195" cy="134" r="2.2"/><circle cx="236" cy="134" r="2.2"/><circle cx="277" cy="134" r="2.2"/>
    </g>
    <g font-size="8" font-weight="600" text-anchor="middle">
      <text x="73" y="96" fill="var(--mint)">Jan</text><text x="114" y="96" fill="var(--blue)">Feb</text><text x="155" y="96" fill="var(--mint)">Mar</text><text x="196" y="96" fill="var(--blue)">Apr</text><text x="237" y="96" fill="var(--mint)">May</text><text x="278" y="96" fill="var(--blue)">Jun</text>
      <text x="73" y="126" fill="var(--mint)">Dec</text><text x="114" y="126" fill="var(--blue)">Nov</text><text x="155" y="126" fill="var(--mint)">Oct</text><text x="196" y="126" fill="var(--blue)">Sep</text><text x="237" y="126" fill="var(--mint)">Aug</text><text x="278" y="126" fill="var(--blue)">Jul</text>
    </g>
  </svg>
  <div class="foot-band">www.nestcourse.com</div><div class="page-no">10</div>
</section>

<!-- 11 Two columns -->
<section class="slide" style="left:419px;top:693px">
  <div class="title" style="left:11px;top:12px">Text Added Here</div>
  <div class="bar" style="left:11px;top:30px"></div>
  <div class="h mint-t" style="left:28px;top:48px;font-size:6.4px;font-weight:500">1. Text Added Here</div>
  <p class="p" style="left:28px;top:57px;width:150px;font-size:3.7px;text-align:justify">Lorem ipsum dolor sit amet, cons ectetuer adipiscing elit, sed diam nonummy nibh euismod tincidunt ut laoreet dolore magna aliquam erat volutpat. Ut wisi enim ad minim veniam, quis nostrud exerci tation ullamcorper suscipit lobortis nisl ut aliquip ex ea commodo consequat.</p>
  <p class="p" style="left:28px;top:88px;width:150px;font-size:3.7px;text-align:justify">Lorem ipsum dolor sit amet, cons ectetuer adipiscing elit, sed diam nonummy nibh euismod tincidunt ut laoreet dolore magna aliquam erat volutpat. Ut wisi enim ad minim veniam, quis nostrud exerci tation ullamcorper suscipit lobortis nisl ut aliquip</p>
  <div class="h mint-t" style="left:188px;top:48px;font-size:6.4px;font-weight:500">2. Text Added Here</div>
  <p class="p" style="left:188px;top:57px;width:150px;font-size:3.7px;text-align:justify">Lorem ipsum dolor sit amet, cons ectetuer adipiscing elit, sed diam nonummy nibh euismod tincidunt ut laoreet dolore magna aliquam erat volutpat. Ut wisi enim ad minim veniam, quis nostrud exerci tation ullamcorper suscipit lobortis nisl ut aliquip ex ea commodo consequat.</p>
  <p class="p" style="left:188px;top:88px;width:150px;font-size:3.7px;text-align:justify">Lorem ipsum dolor sit amet, cons ectetuer adipiscing elit, sed diam nonummy nibh euismod tincidunt ut laoreet dolore magna aliquam erat volutpat. Ut wisi enim ad minim veniam, quis nostrud exerci tation ullamcorper suscipit lobortis nisl ut aliquip</p>
  <svg class="full" viewBox="0 0 365 204">
    <rect x="31" y="124" width="14" height="14" fill="var(--blue)"/><rect x="31" y="156" width="14" height="14" fill="var(--mint)"/>
    <rect x="191" y="124" width="14" height="14" fill="var(--mint)"/><rect x="191" y="156" width="14" height="14" fill="var(--blue)"/>
    <g fill="#fff" font-size="9" font-weight="600" text-anchor="middle"><text x="38" y="134.5">1.</text><text x="38" y="166.5">2.</text><text x="198" y="134.5">1.</text><text x="198" y="166.5">2.</text></g>
    <g font-size="6.2" font-weight="500" fill="var(--ink)"><text x="52" y="128">Lorem ipsum</text><text x="52" y="160">Lorem ipsum</text><text x="212" y="128">Lorem ipsum</text><text x="212" y="160">Lorem ipsum</text></g>
    <g font-size="3.3" fill="var(--gray)">
      <text x="52" y="134">Lorem ipsum dolor sit amet, consectetuer adipiscing elit,</text><text x="52" y="139">sed diam nonummy nibh euismod tincid</text>
      <text x="52" y="166">Lorem ipsum dolor sit amet, consectetuer adipiscing elit,</text><text x="52" y="171">sed diam nonummy nibh euismod tincid</text>
      <text x="212" y="134">Lorem ipsum dolor sit amet, consectetuer adipiscing elit,</text><text x="212" y="139">sed diam nonummy nibh euismod tincid</text>
      <text x="212" y="166">Lorem ipsum dolor sit amet, consectetuer adipiscing elit,</text><text x="212" y="171">sed diam nonummy nibh euismod tincid</text>
    </g>
  </svg>
  <div class="foot-band">www.nestcourse.com</div><div class="page-no">11</div>
</section>

<!-- 12 Costs -->
<section class="slide" style="left:793px;top:693px">
  <div class="title" style="left:11px;top:12px">Company Costs</div>
  <div class="bar" style="left:11px;top:30px"></div>
  <svg class="full" viewBox="0 0 365 204">
    <path d="M65 98H325" stroke="var(--mint)" stroke-width="4.5"/>
    <path d="M108 98h54M236 98h54" stroke="var(--blue)" stroke-width="4.5" opacity=".0"/>
    <path d="M325 93l7 5-7 5z" fill="var(--blue)"/>
    <path d="M300 98h25" stroke="var(--blue)" stroke-width="4.5"/>
    <path d="M172 98h40" stroke="var(--mint)" stroke-width="4.5"/>
    <g fill="none" stroke-width="5">
      <path d="M65 98a22 22 0 0 1 44 0" stroke="var(--mint)"/>
      <path d="M129 98a22 22 0 0 1 44 0" stroke="var(--blue)"/>
      <path d="M193 98a22 22 0 0 1 44 0" stroke="var(--mint)"/>
      <path d="M257 98a22 22 0 0 1 44 0" stroke="var(--blue)"/>
    </g>
    <g fill="#fff"><circle cx="87" cy="77" r="14"/><circle cx="151" cy="77" r="14"/><circle cx="215" cy="77" r="14"/><circle cx="279" cy="77" r="14"/></g>
    <circle cx="87" cy="77" r="7" fill="none" stroke="#3d4148" stroke-width="1.2"/><path d="M87 72.5V77l3 2" fill="none" stroke="#3d4148" stroke-width="1.1"/>
    <path d="M147 72h8l-1 2c3 2 4 5 4 7a3 3 0 0 1-3 3h-8a3 3 0 0 1-3-3c0-2 1-5 4-7z" fill="#3d4148"/>
    <text x="151" y="82" font-size="5.5" fill="#fff" text-anchor="middle" font-weight="600">$</text>
    <g fill="#3d4148"><ellipse cx="215" cy="72" rx="6" ry="2"/><rect x="209" y="73.6" width="12" height="2" rx="1"/><rect x="209" y="76.4" width="12" height="2" rx="1"/><rect x="209" y="79.2" width="12" height="2" rx="1"/></g>
    <circle cx="280" cy="75.5" r="3.6" fill="none" stroke="#3d4148" stroke-width="1.3"/><path d="M277.4 78.2l-3.4 3.4" stroke="#3d4148" stroke-width="1.6"/>
    <g font-size="3.4" fill="#fff" font-weight="600" text-anchor="middle"><text x="96" y="99.3">Step 01</text><text x="160" y="99.3">Step 02</text><text x="224" y="99.3">Step 03</text><text x="290" y="99.3">Step 04</text></g>
    <g stroke="#3d4148" stroke-width=".8"><path d="M87 105v9M151 105v9M215 105v9M279 105v9"/></g>
    <g fill="#3d4148"><circle cx="87" cy="105" r="1"/><circle cx="87" cy="114" r="1"/><circle cx="151" cy="105" r="1"/><circle cx="151" cy="114" r="1"/><circle cx="215" cy="105" r="1"/><circle cx="215" cy="114" r="1"/><circle cx="279" cy="105" r="1"/><circle cx="279" cy="114" r="1"/></g>
    <g font-size="6.4" font-weight="600" fill="var(--ink)" text-anchor="middle"><text x="87" y="124">Lorem Ipsum</text><text x="151" y="124">Lorem Ipsum</text><text x="215" y="124">Lorem Ipsum</text><text x="279" y="124">Lorem Ipsum</text></g>
    <g font-size="2.7" fill="var(--gray)" text-anchor="middle">
      <text x="87" y="129">Lorem ipsum dolor sit</text><text x="87" y="132.5">amet, consectetuer</text><text x="87" y="136">adipiscing elit, sed diam</text><text x="87" y="139.5">nonummy nibh</text><text x="87" y="143">euismod tincidunt ut</text><text x="87" y="146.5">laoreet dolore magna</text><text x="87" y="150">aliquam erat volutpat. Ut</text>
      <text x="151" y="129">Lorem ipsum dolor sit</text><text x="151" y="132.5">amet, consectetuer</text><text x="151" y="136">adipiscing elit, sed diam</text><text x="151" y="139.5">nonummy nibh</text><text x="151" y="143">euismod tincidunt ut</text><text x="151" y="146.5">laoreet dolore magna</text><text x="151" y="150">aliquam erat volutpat. Ut</text>
      <text x="215" y="129">Lorem ipsum dolor sit</text><text x="215" y="132.5">amet, consectetuer</text><text x="215" y="136">adipiscing elit, sed diam</text><text x="215" y="139.5">nonummy nibh</text><text x="215" y="143">euismod tincidunt ut</text><text x="215" y="146.5">laoreet dolore magna</text><text x="215" y="150">aliquam erat volutpat. Ut</text>
      <text x="279" y="129">Lorem ipsum dolor sit</text><text x="279" y="132.5">amet, consectetuer</text><text x="279" y="136">adipiscing elit, sed diam</text><text x="279" y="139.5">nonummy nibh</text><text x="279" y="143">euismod tincidunt ut</text><text x="279" y="146.5">laoreet dolore magna</text><text x="279" y="150">aliquam erat volutpat. Ut</text>
    </g>
  </svg>
  <div class="foot-band">www.nestcourse.com</div><div class="page-no">12</div>
</section>

<!-- 13 Phones -->
<section class="slide" style="left:43px;top:910px">
  <div class="title" style="left:15px;top:12px">Text Added Here</div>
  <div class="bar" style="left:15px;top:30px"></div>
  <p class="p" style="left:15px;top:38px;width:125px;font-size:3.7px">Lorem ipsum dolor sit amet, consectetuer adipiscing elit, sed diam nonummy nibh euismod tincidunt ut laoreet dolore magna aliquam erat volutpat. Ut wisi enim ad minim veniam,</p>
  <p class="p" style="left:15px;top:65px;width:125px;font-size:3.7px">quis nostrud exerci tation ullamcorper suscipit lobortis nisl ut aliquip ex ea commodo consequat. Duis autem vel eum iriure dolor in hendrerit in vulputate velit esse</p>
  <p class="p" style="left:15px;top:88px;width:125px;font-size:3.7px">Lorem ipsum dolor sit amet, consectetuer adipiscing elit, sed diam nonummy nibh euismod tincidunt ut laoreet dolore magna aliquam erat volutpat. Ut wisi enim ad</p>
  <div role="img" aria-label="Faint world map in the background" style="left:150px;top:40px;width:205px;height:130px;background:radial-gradient(ellipse at center,#f0f1f3 0%,#f6f7f8 55%,#fff 100%)"></div>
  <svg class="full" viewBox="0 0 365 204">
    <rect x="29" y="118" width="10" height="10" fill="var(--blue)"/><rect x="29" y="140" width="10" height="10" fill="var(--mint)"/><rect x="29" y="163" width="10" height="10" fill="var(--blue)"/>
    <g fill="#fff" font-size="6.4" font-weight="600" text-anchor="middle"><text x="34" y="125.5">1.</text><text x="34" y="147.5">2.</text><text x="34" y="170.5">3.</text></g>
    <g font-size="4.6" font-weight="600" fill="var(--ink)"><text x="43" y="121">Lorem ipsum</text><text x="43" y="143">Lorem ipsum</text><text x="43" y="166">Lorem ipsum</text></g>
    <g font-size="2.6" fill="var(--gray)">
      <text x="43" y="126">Lorem ipsum dolor sit amet, consectetuer adipiscing elit, sed</text><text x="43" y="129.5">diam nonummy nibh euismod tincid</text>
      <text x="43" y="148">Lorem ipsum dolor sit amet, consectetuer adipiscing elit, sed</text><text x="43" y="151.5">diam nonummy nibh euismod tincid</text>
      <text x="43" y="171">Lorem ipsum dolor sit amet, consectetuer adipiscing elit, sed</text><text x="43" y="174.5">diam nonummy nibh euismod tincid</text>
    </g>
    <g fill="#fff" stroke="#2f333a" stroke-width="1.4">
      <rect x="169" y="29" width="43" height="92" rx="4"/>
      <rect x="225" y="57" width="43" height="92" rx="4"/>
      <rect x="281" y="88" width="43" height="92" rx="4"/>
    </g>
    <g fill="#2f333a"><rect x="184" y="30.5" width="13" height="2" rx="1"/><rect x="240" y="58.5" width="13" height="2" rx="1"/><rect x="296" y="89.5" width="13" height="2" rx="1"/></g>
    <g font-size="5.2" fill="var(--ink)">
      <text x="174" y="45">Lorem</text><text x="174" y="51">ipsum dolor</text>
      <text x="230" y="79">Dolor sit</text><text x="230" y="85">amet, conse</text>
      <text x="286" y="111">Consec</text>
    </g>
    <g stroke="var(--ink)" stroke-width=".5" stroke-dasharray=".8 1.2"><path d="M174 55h14M230 89h14M286 114h14"/></g>
    <g fill="none" stroke="var(--blue)" stroke-width=".7"><rect x="187" y="63" width="6" height="5"/><path d="M241 100l4-4 3 3M241 103h6"/><circle cx="302" cy="127" r="3"/></g>
    <g font-size="2.3" fill="var(--gray)">
      <text x="174" y="79">To introduce the</text><text x="174" y="82">students to the</text><text x="174" y="85">changing landscape of</text><text x="174" y="88">marketing and equip</text><text x="174" y="91">them with knowledge</text><text x="174" y="94">and tools to navigate the</text><text x="174" y="97">digital marketing world.</text>
      <text x="230" y="115">You will learn concepts</text><text x="230" y="118">and ideas in digital</text><text x="230" y="121">marketing as well as</text><text x="230" y="124">how to use different</text><text x="230" y="127">tools and strategies to</text><text x="230" y="130">optimize your digital</text><text x="230" y="133">marketing campaigns.</text>
      <text x="286" y="142">You are required to pass</text><text x="286" y="145">80% of the evaluation</text><text x="286" y="148">test to obtain the</text><text x="286" y="151">certificate. The</text><text x="286" y="154">evaluation test can only</text><text x="286" y="157">be taken 3 times.</text>
    </g>
  </svg>
  <div class="foot-band">www.nestcourse.com</div><div class="page-no">13</div>
</section>

<!-- 14 Team -->
<section class="slide" style="left:419px;top:910px">
  <div class="title" style="left:17px;top:12px">Our Team Members</div>
  <div class="bar" style="left:17px;top:30px"></div>
  <p class="p" style="left:17px;top:37px;width:333px;font-size:3.7px">Lorem ipsum dolor sit amet, consectetuer adipiscing elit, sed diam nonummy nibh euismod tincidunt ut laoreet dolore magna aliquam erat volutpat. Ut wisi enim ad minim veniam, quis nostrud exerci tation ullamcorper suscipit lobortis nisl ut aliquip ex ea commodo consequat. Duis autem vel eum iriure dolor in hendrerit in vulputate velit esse molestie consequat, vel illum dolore eu feugiat nulla facilisis at vero eros et accumsan et iusto odio dignissim qui blandit praesent luptatum zzril delenit augue duis dolore te feugait nulla facilisi.</p>
  <p class="p" style="left:17px;top:63px;width:333px;font-size:3.7px">Lorem ipsum dolor sit amet, cons ectetuer adipiscing elit, sed diam nonummy nibh euismod tincidunt ut laoreet dolore magna aliquam erat volutpat. Ut wisi enim ad minim veniam, quis nostrud exerci tation ullamcorper suscipit lobortis nisl ut aliquip ex</p>
  <svg class="full" viewBox="0 0 365 204">
    <g fill="none" stroke="var(--mint)" stroke-width="1.4"><circle cx="50" cy="113" r="16"/><circle cx="138" cy="113" r="16"/><circle cx="224" cy="113" r="16"/><circle cx="312" cy="113" r="16"/></g>
    <g fill="#d7d9dc"><circle cx="50" cy="113" r="13.5"/><circle cx="138" cy="113" r="13.5"/><circle cx="224" cy="113" r="13.5"/><circle cx="312" cy="113" r="13.5"/></g>
    <g font-size="6" font-weight="600" fill="var(--mint)" text-anchor="middle"><text x="50" y="137">ALEX REED</text><text x="138" y="137">NORA BELL</text><text x="224" y="137">ALEX REED</text><text x="312" y="137">NORA BELL</text></g>
    <g font-size="2.7" fill="var(--gray)" text-anchor="middle">
      <text x="50" y="142">ipsum dolor sit amet, cons</text><text x="50" y="145.5">ectetuer adipiscing elit, sed</text><text x="50" y="149">diam nonummy nibh</text><text x="50" y="152.5">euismod tincidunt ut</text><text x="50" y="156">laoreet dolore magna</text><text x="50" y="159.5">aliquam erat volutpat. Ut</text><text x="50" y="163">wisi enim ad minim veniam,</text><text x="50" y="166.5">quis nostrud</text>
      <text x="138" y="142">ipsum dolor sit amet, cons</text><text x="138" y="145.5">ectetuer adipiscing elit, sed</text><text x="138" y="149">diam nonummy nibh</text><text x="138" y="152.5">euismod tincidunt ut</text><text x="138" y="156">laoreet dolore magna</text><text x="138" y="159.5">aliquam erat volutpat. Ut</text><text x="138" y="163">wisi enim ad minim veniam,</text><text x="138" y="166.5">quis nostrud</text>
      <text x="224" y="142">ipsum dolor sit amet, cons</text><text x="224" y="145.5">ectetuer adipiscing elit, sed</text><text x="224" y="149">diam nonummy nibh</text><text x="224" y="152.5">euismod tincidunt ut</text><text x="224" y="156">laoreet dolore magna</text><text x="224" y="159.5">aliquam erat volutpat. Ut</text><text x="224" y="163">wisi enim ad minim veniam,</text><text x="224" y="166.5">quis nostrud</text>
      <text x="312" y="142">ipsum dolor sit amet, cons</text><text x="312" y="145.5">ectetuer adipiscing elit, sed</text><text x="312" y="149">diam nonummy nibh</text><text x="312" y="152.5">euismod tincidunt ut</text><text x="312" y="156">laoreet dolore magna</text><text x="312" y="159.5">aliquam erat volutpat. Ut</text><text x="312" y="163">wisi enim ad minim veniam,</text><text x="312" y="166.5">quis nostrud</text>
    </g>
  </svg>
  <div class="foot-band">www.nestcourse.com</div><div class="page-no">14</div>
</section>

<!-- 15 Thank you -->
<section class="slide no-rule" style="left:793px;top:910px">
  <div class="corner mint" style="left:11px;top:8px"></div>
  <div class="photo photo-blue" role="img" aria-label="Soft blue-tinted photo of a smiling baby lying on a bed" style="left:0;top:33px;width:365px;height:138px"></div>
  <div class="roboto" style="left:90px;top:80px;font-size:37px;font-weight:700;color:#fff;letter-spacing:-.3px">Thank You</div>
</section>

</body>
</html>
```